Winter Carnival - FUN Web Design Project

The winter carnival is celebrating it's 50th anniversary this year and we are looking to have a new website that will not only work for the 50th, but will work for future years as well (so cannot be 100% geared to the anniversary in terms of look & feel).

The primary focus of the Carnival is the events that take place through the 10-day carnival, and giving recognition to the sponsors (rotating logos on splash page / interior).

The primary colours of the Carnival are Red and White. For some background information - see the old site parked here: http://www.plavetro.on.ca/content.php?ID=34

For the design concepts, we welcome stock photography as we would like to see several photos located prominently throughout the site which we will provide once the site is being constructed (no need to buy stock - we have lots of photos that we can use once a design is selected).

The carnival is a WINTER carnival - so obviously a winter theme utilizing the Red / White colours of our brand.

PSD files will be required so we can code the site to our needs from a technical perspective.
Updates

Good quality GIF of logo attached with lower-quality (sorry) version of the Wordmark uploaded to Project File.

Date extended 1 day to Sunday!

Industry/Entity Type

Events

Requirements
Must have
• Prominent placement for key sponsor logos
Links to social media - PageRing / Chirplo / Boardlyn
Photo-friendly website
Incorporation of corporate colours - Red / White
1 x Home/Splash page layout - emphasis on sponsors, photos, featured event
1 x Interior page layout - more focused on content - see http://www.plavetro.on.ca/content.php?ID=34
Site search bar
Drop-down navigation / changing colour rollovers
Child - Friendly

Nice to have
• Banner/Image links to other site features:
- news
- photo gallery
- History

```html
<!DOCTYPE html>
<html lang="en">
<head>
<meta charset="utf-8">
<title>Plavetro Winter Carnival</title>
<link href="https://fonts.googleapis.com/css2?family=Arimo:wght@400;700&display=swap" rel="stylesheet">
<style>
:root{
  --red:#d0121f;
  --red-dark:#9e0b14;
  --blue:#3b7fd1;
  --text:#3d3d3d;
  --muted:#666;
  --line:#dcdcdc;
  --band:#f2f2f2;
  --sky:#9cc6ea;
  --white:#fff;
}
*{box-sizing:border-box;margin:0;padding:0}
html,body{width:988px;height:1200px;overflow:hidden}
body{font-family:"Arimo",Arial,sans-serif;color:var(--text);background:#eef4fa}
.stage{position:absolute;left:0;top:0;width:1200px;height:1458px;transform:scale(.82333);transform-origin:0 0;
  background:linear-gradient(90deg,var(--sky) 0%,#dbe9f5 13%,#f4f8fb 50%,#dbe9f5 87%,#b7d5ee 100%)}
.page{position:absolute;left:160px;top:0;width:880px;height:1458px;background:var(--white)}
.abs{position:absolute}
a{text-decoration:none;color:inherit}

.mascot{left:215px;top:100px;width:70px;height:90px;border-radius:40% 40% 20% 20%;background:linear-gradient(#f3f3f3,#e3343e)}
.bubble{left:300px;top:50px;width:140px;height:80px;border:1px solid #e2e2e2;border-radius:8px;background:#fff;box-shadow:0 1px 4px rgba(0,0,0,.08);
  font-size:11px;line-height:17px;color:#555;padding:12px 10px}
.sponsor-note{left:740px;top:95px;width:240px;text-align:right;font-size:11px;color:#444}
.round-btn{width:26px;height:26px;border-radius:50%;border:1px solid #ddd;background:#fafafa;box-shadow:0 1px 2px rgba(0,0,0,.1)}
.sponsor-name{left:835px;top:142px;font-size:24px;color:#222;display:flex;align-items:center;gap:6px}
.sponsor-name i{display:inline-block;width:12px;height:12px;border-radius:50%;background:#222}

.nav{left:147px;top:190px;width:893px;height:36px;background:linear-gradient(#df1a26,#c70f1b)}
.nav-fold{left:147px;top:178px;width:13px;height:12px;background:linear-gradient(135deg,transparent 50%,var(--red-dark) 50%)}
.nav a{position:absolute;top:10px;font-size:13px;color:#fff}
.nav-pointer{left:410px;top:221px;width:0;height:0;border:6px solid transparent;border-bottom-color:#fff;border-top:0}
.search{left:832px;top:195px;width:155px;height:26px;border-radius:13px;background:#fff;font-size:11px;color:#555;padding:7px 12px}
.search-btn{left:963px;top:197px;width:22px;height:22px;border-radius:50%;background:var(--red)}

.crumb{left:160px;top:226px;width:880px;height:30px;background:var(--band);font-size:10px;color:#555}
.crumb .here{position:absolute;left:48px;top:10px}
.crumb .follow{position:absolute;right:50px;top:10px;display:flex;gap:8px}
.crumb .follow span.net{color:var(--blue)}

.bar{left:208px;width:782px;height:36px;border-radius:8px;background:linear-gradient(#fff,#f1f1f1);box-shadow:0 1px 3px rgba(0,0,0,.12)}
.bar-title{font-size:15px;color:var(--blue)}
.item-title{font-size:15px;color:var(--red)}
.small-title{font-size:13px;color:var(--red)}
.date{font-size:9px;color:#666}
.copy{font-size:11px;line-height:19px;color:#444}
.more{color:var(--blue)}
.more::after{content:"";display:inline-block;margin-left:7px;border:4px solid transparent;border-left-color:var(--blue);border-right:0;vertical-align:-1px}
.photo{border-radius:6px}
.btn{height:30px;border-radius:5px;background:linear-gradient(#e11c28,#bf0d18);color:#fff;font-size:11px;text-align:center;line-height:30px;box-shadow:0 1px 2px rgba(0,0,0,.2)}
.arrow{width:36px;height:36px;border-radius:50%;background:#fff;box-shadow:0 1px 4px rgba(0,0,0,.25)}
.chev{position:absolute;left:14px;top:13px;width:9px;height:9px;border-left:2px solid #333;border-bottom:2px solid #333;transform:rotate(45deg)}
.chev.right{left:11px;transform:rotate(-135deg)}

.gallery-cta{left:251px;top:1020px;width:176px;height:176px;border-radius:50%;background:rgba(38,44,54,.88);color:#fff;font-size:19px;line-height:29px;padding:56px 0 0 29px}

.footer-rule{left:208px;top:1264px;width:780px;height:1px;background:var(--line)}
.footer-copy{left:208px;top:1277px;font-size:11px;color:#444}
.footer-copy span{color:var(--red)}
.footer-links{left:690px;top:1277px;font-size:11px;color:#444;display:flex;gap:10px}
.badge{background:#e8e8e8;border-radius:4px}
</style>
</head>
<body>
<div class="stage">
  <div class="page"></div>

  <header>
    <div class="abs mascot" role="img" aria-label="Carnival mascot illustration"></div>
    <div class="abs bubble">Welcome to Northvale's Winter Carnival Plavetro. See our gallery! :)</div>
    <p class="abs sponsor-note">We say 'thank you' to all our sponsors:</p>
    <div class="abs round-btn" style="left:784px;top:141px"><span class="chev" style="left:10px;top:8px;width:7px;height:7px;border-width:1.5px"></span></div>
    <div class="abs sponsor-name"><i></i>Northvale</div>
    <div class="abs round-btn" style="left:963px;top:141px"><span class="chev right" style="left:7px;top:8px;width:7px;height:7px;border-width:1.5px"></span></div>
  </header>

  <div class="abs nav-fold"></div>
  <nav class="abs nav">
    <svg class="abs" style="left:60px;top:12px" width="12" height="12" viewBox="0 0 12 12"><path d="M6 1 0 6.5h1.8V11h3V8h2.4v3h3V6.5H12z" fill="#fff"/></svg>
    <a style="left:98px">Home</a>
    <a style="left:162px">Events</a>
    <a style="left:231px">Photo Gallery</a>
    <a style="left:340px">Sponsors</a>
    <a style="left:425px">Carnival Info</a>
    <a style="left:528px">Contact us</a>
  </nav>
  <div class="abs nav-pointer"></div>
  <div class="abs search">Search your phrase...</div>
  <div class="abs search-btn"><svg width="22" height="22" viewBox="0 0 22 22"><circle cx="10" cy="10" r="3.5" fill="none" stroke="#fff" stroke-width="1.6"/><path d="M12.5 12.5 15 15" stroke="#fff" stroke-width="1.8"/></svg></div>

  <div class="abs crumb">
    <span class="here">You are here: Home</span>
    <span class="follow">Follow us on: <span class="net">PageRing</span><span class="net">Chirplo</span><span class="net">Boardlyn</span><span class="net">Tubely</span></span>
  </div>

  <main>
    <div class="abs bar" style="top:284px"></div>
    <h2 class="abs bar-title" style="left:228px;top:294px;font-weight:400">Latest news</h2>
    <h2 class="abs bar-title" style="left:621px;top:294px;font-weight:400">Latest photos</h2>

    <article>
      <h3 class="abs item-title" style="left:228px;top:328px;font-weight:400">Thank You, Volunteers!</h3>
      <p class="abs date" style="left:230px;top:348px">DATE: 11.12.2012.</p>
      <div class="abs photo" style="left:228px;top:365px;width:343px;height:106px;background:linear-gradient(90deg,#3f63c8,#cfe3f2 60%,#a9cde6)" role="img" aria-label="Snow mascot in front of an ice palace"></div>
      <p class="abs copy" style="left:229px;top:477px;width:345px">Plavetro is delighted to recognize Volunteer Week 2013! We are powered by Volunteers; starting with the 11 dedicated Directors on our own Board, right through to the 509... <a class="more">see details</a></p>
    </article>
    <a class="abs btn" style="left:484px;top:552px;width:93px">Read all news</a>

    <div class="abs photo" style="left:621px;top:330px;width:344px;height:142px;background:linear-gradient(#b9c9d4,#e9eef2 60%,#f6f8fa)" role="img" aria-label="Mascot with visitors in the snow"></div>
    <div class="abs arrow" style="left:603px;top:388px"><span class="chev"></span></div>
    <div class="abs arrow" style="left:948px;top:388px"><span class="chev right"></span></div>
    <p class="abs copy" style="left:624px;top:477px;width:340px">It is a long established fact that a reader will be distracted by the readable content of a page when looking at its layout.<br><span style="color:var(--red)">Click on the picture to zoom.</span></p>

    <div class="abs bar" style="top:614px"></div>
    <h2 class="abs bar-title" style="left:228px;top:624px;font-weight:400">Events</h2>
    <h2 class="abs bar-title" style="left:621px;top:624px;font-weight:400">Newest Winter Carnival's video</h2>

    <article>
      <div class="abs photo" style="left:228px;top:663px;width:92px;height:85px;background:linear-gradient(#c7d3dc,#e7b7c4)" role="img" aria-label="Polar bear swim participants"></div>
      <h3 class="abs small-title" style="left:331px;top:662px;font-weight:400">Polar Bear swims</h3>
      <p class="abs date" style="left:331px;top:679px">DATE: 11.12.2012</p>
      <p class="abs copy" style="left:331px;top:692px;width:250px">Lorem Ipsum is simply dummy text of the printing and typesetting industry. Lorem Ipsum has been the industry's standard... <a class="more">see details</a></p>
    </article>
    <article>
      <div class="abs photo" style="left:228px;top:764px;width:92px;height:86px;background:linear-gradient(#6b4a2b,#3b2a5c)" role="img" aria-label="Costumed mascot at an event"></div>
      <h3 class="abs small-title" style="left:331px;top:763px;font-weight:400">Mascot scate</h3>
      <p class="abs date" style="left:331px;top:780px">DATE: 11.12.2012</p>
      <p class="abs copy" style="left:331px;top:793px;width:250px">There are many variations of passages of Lorem Ipsum available, but the majority have suffered alteration in some form, <a class="more">see details</a></p>
    </article>
    <a class="abs btn" style="left:485px;top:872px;width:93px">See all events</a>

    <div class="abs photo" style="left:621px;top:661px;width:344px;height:107px;background:linear-gradient(#4b4f55,#8a9097 55%,#c9ced3)" role="img" aria-label="Video still of skaters on an outdoor rink"></div>
    <svg class="abs" style="left:767px;top:691px" width="50" height="50" viewBox="0 0 50 50"><circle cx="25" cy="25" r="23" fill="rgba(30,30,30,.45)" stroke="#fff" stroke-width="2"/><path d="M20 16v18l14-9z" fill="#fff"/></svg>

    <h2 class="abs bar-title" style="left:624px;top:784px;font-weight:400">Sign up to our newsletter <svg width="10" height="6" viewBox="0 0 10 6" style="margin-left:4px;vertical-align:3px"><path d="M0 0h10L5 6z" fill="#3b7fd1"/></svg></h2>
    <p class="abs copy" style="left:624px;top:810px;width:285px">All the Lorem Ipsum generators on the Internet tend to repeat predefined chunks as necessary, making this the first true generator on the Internet.</p>
    <div class="abs" style="left:623px;top:880px;width:190px;height:32px;border-radius:16px;border:1px solid #ddd;background:#fff;box-shadow:inset 0 1px 3px rgba(0,0,0,.12);font-size:11px;color:#555;padding:9px 15px">Write your e-mail here...</div>
    <div class="abs" style="left:791px;top:882px;width:28px;height:28px;border-radius:50%;background:var(--red);color:#fff;font-size:10px;text-align:center;line-height:28px">OK</div>

    <div class="abs bar" style="top:942px"></div>
    <h2 class="abs bar-title" style="left:228px;top:951px;font-weight:400">Photo gallery</h2>
    <div class="abs photo" style="left:208px;top:988px;width:780px;height:230px;background:linear-gradient(90deg,#8fb0d4,#d6e6f1 45%,#c8dbe9 75%,#eef4f8)" role="img" aria-label="Snow mascot with a gnome by the ice palace"></div>
    <a class="abs gallery-cta">Click here to<br>see our gallery</a>
  </main>

  <footer>
    <div class="abs footer-rule"></div>
    <p class="abs footer-copy">Copyright by <span>Northvale's Winter Carnival 2012</span>. All rights reserved.</p>
    <nav class="abs footer-links"><a>Home</a><a>Events</a><a>Gallery</a><a>Sponsors</a><a>Carnival Info</a><a>Contact</a></nav>
    <div class="abs" style="left:214px;top:1346px;font-size:24px;color:#666;display:flex;align-items:center;gap:6px"><i style="display:inline-block;width:12px;height:12px;border-radius:50%;background:#888"></i>Northvale</div>
    <div class="abs badge" style="left:392px;top:1330px;width:78px;height:68px"></div>
    <div class="abs badge" style="left:535px;top:1328px;width:140px;height:62px"></div>
    <div class="abs badge" style="left:737px;top:1328px;width:94px;height:50px"></div>
    <div class="abs badge" style="left:884px;top:1328px;width:110px;height:62px"></div>
  </footer>
</div>
</body>
</html>
```